agricultural technology company needs business cards*

design a business card that represents our business well. please see our website: vastrelbyfieldseal.com.au
professional, simple, clean lines, not complicated or floral.....

```html
<!DOCTYPE html>
<html lang="en">
<head>
<meta charset="utf-8">
<title>Vastrel Byfield Seal – Business Card</title>
<link rel="stylesheet" href="https://fonts.googleapis.com/css2?family=Montserrat:wght@400;500;600;700&display=swap">
<style>
  :root {
    --backdrop: #d0d0d0;
    --card: #ffffff;
    --tint: #f6f7fa;
    --navy: #1f2f66;
    --green: #2aa845;
    --lime: #a3c93a;
  }
  * { box-sizing: border-box; margin: 0; padding: 0; }
  html, body {
    width: 1200px; height: 933px; overflow: hidden;
    background: var(--backdrop);
    font-family: "Montserrat", Arial, sans-serif;
  }
  .card {
    position: absolute; left: 321px; width: 558px; height: 320px;
    background: var(--card); overflow: hidden;
  }
  .card--front { top: 87px; }
  .card--back { top: 467px; }
  .card__tint { position: absolute; inset: 0; width: 558px; height: 320px; }

  .brand {
    position: absolute; left: 0; right: 0; top: 118px;
    display: flex; align-items: center; justify-content: center; gap: 14px;
  }
  .brand__mark { width: 22px; height: 22px; background: var(--green); }
  .brand__name {
    font-weight: 700; font-size: 30px; line-height: 1.05;
    color: var(--navy); letter-spacing: -0.5px;
  }

  .person {
    position: absolute; left: 0; width: 289px; top: 144px; text-align: center;
    color: var(--navy);
  }
  .person__name { font-weight: 600; font-size: 20px; line-height: 24px; }
  .person__role { font-weight: 500; font-size: 11.5px; line-height: 16px; }

  .divider {
    position: absolute; left: 288px; top: 90px; width: 1px; height: 144px;
    background: var(--green);
  }
  .contact { position: absolute; left: 319px; top: 128px; list-style: none; color: var(--navy); }
  .contact__item {
    display: flex; align-items: flex-start; gap: 10px;
    font-size: 11.2px; font-weight: 500; line-height: 15px; margin-bottom: 10px;
  }
  .contact__icon { width: 12px; height: 12px; flex: none; margin-top: 1px; }
</style>
</head>
<body>

<section class="card card--front">
  <svg class="card__tint" viewBox="0 0 558 320" aria-hidden="true">
    <polygon points="225,0 558,0 558,320 542,320" fill="var(--tint)"/>
  </svg>
  <div class="brand">
    <span class="brand__mark"></span>
    <span class="brand__name">Vastrel<br>Byfield Seal</span>
  </div>
</section>

<section class="card card--back">
  <svg class="card__tint" viewBox="0 0 558 320" aria-hidden="true">
    <polygon points="0,0 335,0 17,320 0,320" fill="var(--tint)"/>
  </svg>

  <div class="person">
    <p class="person__name">Maren Oosthuis</p>
    <p class="person__role">Director, Vastrel Byfield Seal</p>
  </div>

  <div class="divider"></div>

  <ul class="contact">
    <li class="contact__item">
      <svg class="contact__icon" viewBox="0 0 12 12" aria-hidden="true">
        <rect x="3.5" y="1" width="5" height="10" rx="0.8" fill="none" stroke="var(--green)" stroke-width="1.2"/>
      </svg>
      <span>1300 482 916</span>
    </li>
    <li class="contact__item">
      <svg class="contact__icon" viewBox="0 0 12 12" aria-hidden="true">
        <g fill="none" stroke="var(--green)" stroke-width="1">
          <circle cx="6" cy="6" r="5"/>
          <ellipse cx="6" cy="6" rx="2.2" ry="5"/>
          <line x1="1" y1="6" x2="11" y2="6"/>
          <line x1="1.8" y1="3.5" x2="10.2" y2="3.5"/>
          <line x1="1.8" y1="8.5" x2="10.2" y2="8.5"/>
        </g>
      </svg>
      <span>vastrelbyfieldseal.com.au</span>
    </li>
    <li class="contact__item">
      <svg class="contact__icon" viewBox="0 0 12 12" aria-hidden="true">
        <path d="M6 11.5 C3.5 8.5 2.2 6.6 2.2 4.6 A3.8 3.8 0 0 1 9.8 4.6 C9.8 6.6 8.5 8.5 6 11.5 Z" fill="none" stroke="var(--green)" stroke-width="1.1"/>
        <circle cx="6" cy="4.6" r="1.3" fill="none" stroke="var(--green)" stroke-width="1"/>
      </svg>
      <span>52 Harlow Road,<br>Merrindale, WA 6170</span>
    </li>
  </ul>
</section>

</body>
</html>
```